Medical Eye Care Practice needs a unique business card design.

I need a business card for my medical, eye care practice. I am seeking a unique design, possibly with a vertical or atypical shape layout -- something to make the card stand out. I would like the final design to communicate health and wellness with a contemporary feel. Please incorporate my logo and slogan with a color scheme based off of my logo. It should also identify all of the information that is listed on my sample business card. The back side should be utilized for appointment reminder with date, time, and room for notes. I would also like some incorporation of facebook, twitter, and google plus links.

```html
<!DOCTYPE html>
<html lang="en">
<head>
<meta charset="utf-8">
<title>Harborview Eye Care – Business Card</title>
<link rel="stylesheet" href="https://fonts.googleapis.com/css2?family=Roboto:wght@400;500&display=swap">
<style>
  :root {
    --backdrop: #3a332c;
    --card-brown: #8a7253;
    --card-white: #ffffff;
    --ink: #2b2b2b;
    --ink-soft: #4a4a4a;
    --tan: #a88a5f;
    --dots: #555;
  }
  * { box-sizing: border-box; margin: 0; padding: 0; }
  html, body { width: 1200px; height: 803px; overflow: hidden; }
  body {
    background: var(--backdrop);
    display: flex;
    align-items: center;
    justify-content: center;
    gap: 70px;
    font-family: "Roboto", Arial, sans-serif;
  }
  .card {
    width: 340px;
    height: 595px;
    position: relative;
    box-shadow: 0 10px 30px rgba(0,0,0,0.35);
  }

  /* Practice name with plain circle */
  .practice-name {
    display: flex;
    align-items: center;
    justify-content: center;
    gap: 10px;
    font-weight: 500;
    white-space: nowrap;
  }
  .practice-name__dot {
    flex: 0 0 auto;
    border-radius: 50%;
  }

  /* Back side */
  .card--back {
    background: var(--card-brown);
    color: #fff;
    display: flex;
    flex-direction: column;
    align-items: center;
    justify-content: center;
    text-align: center;
  }
  .card--back .practice-name { font-size: 26px; }
  .card--back .practice-name__dot { width: 26px; height: 26px; background: #fff; }
  .card--back .website { font-size: 12px; margin-top: 22px; letter-spacing: 0.5px; }

  /* Front side */
  .card--front {
    background: var(--card-white);
    color: var(--ink);
    padding: 40px 30px 34px;
  }
  .card--front .practice-name { font-size: 22px; color: var(--tan); }
  .card--front .practice-name__dot { width: 20px; height: 20px; background: var(--tan); }

  .person { text-align: right; margin-top: 48px; }
  .person__name { font-size: 22px; font-weight: 500; }
  .person__title { font-size: 11px; color: var(--tan); letter-spacing: 1px; margin-top: 2px; }

  .contact { list-style: none; margin-top: 50px; font-size: 12.5px; color: var(--ink-soft); }
  .contact li { display: flex; align-items: flex-start; gap: 8px; margin-bottom: 4px; line-height: 1.25; }
  .contact svg { flex: 0 0 14px; margin-top: 1px; }
  .contact .address { margin-top: 6px; }

  .appointment { margin-top: 44px; font-size: 12.5px; color: var(--ink-soft); }
  .appointment__row { display: flex; align-items: flex-end; gap: 4px; margin-bottom: 16px; }
  .dotted { flex: 1; border-bottom: 1.5px dotted var(--dots); height: 10px; }
</style>
</head>
<body>

  <section class="card card--back" aria-label="Card back">
    <p class="practice-name"><span class="practice-name__dot"></span>Harborview Eye Care</p>
    <p class="website">www.harborview-eye.com</p>
  </section>

  <section class="card card--front" aria-label="Card front">
    <p class="practice-name"><span class="practice-name__dot"></span>Harborview Eye Care</p>

    <div class="person">
      <p class="person__name">Daniel Hart</p>
      <p class="person__title">OD | FAAO</p>
    </div>

    <ul class="contact">
      <li>
        <svg width="14" height="14" viewBox="0 0 14 14" aria-hidden="true"><circle cx="7" cy="7" r="7" fill="var(--tan)"/><path d="M4.5 3.5l1.5 0 .6 1.8-.9.7a5 5 0 0 0 2.3 2.3l.7-.9 1.8.6v1.5c-3.5.3-6.3-2.5-6-6z" fill="#fff"/></svg>
        (555) 014-2207
      </li>
      <li>
        <svg width="14" height="14" viewBox="0 0 14 14" aria-hidden="true"><circle cx="7" cy="7" r="7" fill="var(--tan)"/><rect x="4" y="6" width="6" height="4" fill="#fff"/><rect x="5" y="3.5" width="4" height="2" fill="#fff"/></svg>
        (555) 014-2208
      </li>
      <li>
        <svg width="14" height="14" viewBox="0 0 14 14" aria-hidden="true"><circle cx="7" cy="7" r="7" fill="var(--tan)"/><circle cx="7" cy="7" r="3.5" fill="none" stroke="#fff" stroke-width="1"/><path d="M3.5 7h7M7 3.5v7" stroke="#fff" stroke-width="0.8"/></svg>
        www.harborview-eye.com
      </li>
      <li class="address">
        <svg width="14" height="14" viewBox="0 0 14 14" aria-hidden="true"><circle cx="7" cy="7" r="7" fill="var(--tan)"/><path d="M7 3a2.5 2.5 0 0 1 2.5 2.5C9.5 7.5 7 10.5 7 10.5S4.5 7.5 4.5 5.5A2.5 2.5 0 0 1 7 3z" fill="#fff"/><circle cx="7" cy="5.5" r="0.9" fill="var(--tan)"/></svg>
        <span>418 Orchard Ave. Suite 210<br>Millbrook, WI 53090</span>
      </li>
    </ul>

    <div class="appointment">
      <div class="appointment__row"><span>Date:</span><span class="dotted"></span><span>Time:</span><span class="dotted"></span></div>
      <div class="appointment__row"><span>Room:</span><span class="dotted"></span></div>
      <div class="appointment__row"><span class="dotted"></span></div>
    </div>
  </section>

</body>
</html>
```